Web Design Project (uncoded)

About Us
Tavelko is a telecom startup and is looking to launch its website.
Tavelko specializes in providing communication solutions to the travel market. Our mission is to develop cost effective communication products and solutions for the international traveler.
Our simple vision of "every hotel should have a mobile phone in the guest rooms", led us to develop a pathbreaking & cost effective mobile phone. With full integration capabilities with the hotels property management system, location based marketing, user locator and other features, this product is unique in addressing the hospitality segment.
The website is targeted at hotel owners and property management companies.
The website should have a young contemporary and a funky look, in line with the name.
Please find attached our logo (for the colors etc.). (attached now).
We would like to receive the design for a home page and an inside page for the website.
Site map would be as follows: Home, About Us, Solutions, Contact us
Thanks and look forward,
Tamsa
Target Market(s)
Hotel decision makers
Industry/Entity Type
Property Management
Look and feel
Each slider illustrates characteristics of the customer's brand and the style your logo design should communicate.

```html
<!DOCTYPE html>
<html lang="en">
<head>
<meta charset="utf-8">
<title>Tavelko – Home</title>
<link rel="stylesheet" href="https://fonts.googleapis.com/css2?family=Arimo:wght@400;700&family=Open+Sans:wght@400;600&family=Signika:wght@400;600&display=swap">
<style>
  :root{
    --bg:#8a9e9c;
    --bg-glow:#f4f6f6;
    --orange:#f47f20;
    --orange-dark:#e46f0e;
    --ink:#111111;
    --panel:#eef2f1;
    --white:#ffffff;
    --rule:#9aa3a3;
    --field-border:#cfd5d5;
    --footer-link:#5b6566;
  }
  *{box-sizing:border-box;margin:0;padding:0}
  html,body{width:1176px;height:1200px;overflow:hidden}
  body{
    position:relative;
    background:radial-gradient(ellipse 420px 300px at 588px 170px,var(--bg-glow) 0%,#c9d2d1 45%,var(--bg) 100%);
    font-family:"Arimo",Arial,sans-serif;color:var(--ink);
  }
  .abs{position:absolute}

  .brand{position:absolute;top:66px;left:0;width:1176px;display:flex;justify-content:center;align-items:center;gap:14px}
  .brand-dot{width:91px;height:91px;border-radius:50%;background:var(--orange)}
  .brand-name{font-family:"Arimo",sans-serif;font-weight:700;font-size:58px;color:var(--ink);letter-spacing:-1px}

  .main-nav{left:265px;top:210px;width:646px;height:44px;background:linear-gradient(var(--orange),var(--orange-dark));border-radius:8px 8px 0 0}
  .nav-shadow{left:262px;top:252px;width:652px;height:6px;background:#111;border-radius:0 0 4px 4px}
  .nav-tab{top:205px;left:338px;width:98px;height:49px;background:linear-gradient(#2a2a2a,#050505);border-radius:8px 8px 0 0}
  .nav-link{font-family:"Open Sans",sans-serif;font-size:18px;color:var(--white);top:219px}
  .nav-sep{top:220px;width:1px;height:23px;background:#3a1a00}

  .panel{left:55px;top:258px;width:1066px;height:845px;background:var(--panel);border-radius:5px}
  .slider{left:79px;top:282px;width:1018px;height:374px;background:var(--white);border-radius:9px}

  .heading{font-family:"Signika",sans-serif;font-weight:400;font-size:37px;color:var(--orange);letter-spacing:.3px;line-height:1}
  .field{left:79px;width:346px;height:40px;background:var(--white);border:2px solid var(--field-border);border-radius:7px;overflow:hidden}
  .field-btn{position:absolute;right:0;top:0;width:48px;height:100%;background:#0c0c0c;display:flex;align-items:center;justify-content:center}
  .dotted-h{left:89px;top:808px;width:326px;border-top:2px dotted var(--rule)}
  .dotted-v{left:439px;top:674px;height:382px;border-left:2px dotted var(--rule)}

  .copy{font-size:15.5px;line-height:18px;letter-spacing:.3px}
  .copy p+p{margin-top:18px}
  .news-copy{text-align:justify;hyphens:auto}
  .read-more{left:1013px;top:1046px;font-size:15px;color:var(--orange);display:flex;align-items:center;gap:8px}

  .footer-rule{left:55px;top:1067px;width:1066px;height:2px;background:#c6cccc}
  .footer-nav{top:1076px;font-family:"Open Sans",sans-serif;font-size:13px;color:var(--footer-link);text-decoration:underline}
  .footer-nav.active{color:var(--orange)}
  .panel-shadow{left:262px;top:1103px;width:652px;height:6px;background:#111;border-radius:0 0 4px 4px}

  .footer-brand{left:68px;top:1112px;display:flex;align-items:center;gap:8px}
  .footer-brand .brand-dot{width:40px;height:40px}
  .footer-brand .brand-name{font-size:24px;letter-spacing:-.5px}
  .copyright{right:67px;top:1122px;font-family:"Open Sans",sans-serif;font-size:13px;color:var(--white)}
</style>
</head>
<body>
  <header class="brand">
    <span class="brand-dot"></span>
    <span class="brand-name">Tavelko</span>
  </header>

  <nav>
    <div class="abs main-nav"></div>
    <div class="abs nav-shadow"></div>
    <div class="abs nav-tab"></div>
    <span class="abs nav-link" style="left:361px">Home</span>
    <span class="abs nav-link" style="left:461px">About Us</span>
    <span class="abs nav-sep" style="left:564px"></span>
    <span class="abs nav-link" style="left:589px">Solutions</span>
    <span class="abs nav-sep" style="left:695px"></span>
    <span class="abs nav-link" style="left:719px">Contact Us</span>
  </nav>

  <main>
    <div class="abs panel"></div>
    <div class="abs slider" role="img" aria-label="Home page slider area"></div>

    <h2 class="abs heading" style="left:78px;top:694px">SEARCH</h2>
    <div class="abs field" style="top:745px">
      <span class="field-btn"><svg width="28" height="28" viewBox="0 0 28 28"><circle cx="14" cy="14" r="11" fill="none" stroke="#f47f20" stroke-width="3"/></svg></span>
    </div>
    <div class="abs dotted-h"></div>

    <h2 class="abs heading" style="left:78px;top:835px">SUBSCRIBE</h2>
    <div class="abs field" style="top:883px">
      <span class="field-btn"><svg width="28" height="28" viewBox="0 0 28 28"><circle cx="14" cy="14" r="11" fill="none" stroke="#f47f20" stroke-width="3"/></svg></span>
    </div>

    <div class="abs copy" style="left:79px;top:950px;width:346px">
      <p>Each slider illustrates characteristics of the customer's brand and the style your design should communicate.</p>
      <p>Each slider illustrates characteristics of the</p>
    </div>

    <div class="abs dotted-v"></div>

    <h2 class="abs heading" style="left:454px;top:694px">LATEST NEWS</h2>
    <div class="abs copy news-copy" lang="en" style="left:457px;top:742px;width:641px">
      <p>Tavelko is a telecom startup and is looking to launch its website.</p>
      <p>Tavelko specializes in providing communication solutions to the travel market. Our mission is to develop cost effective communication products and solutions for the international traveler.</p>
      <p>Our simple vision of "every hotel should have a mobile phone in the guest rooms", led us to develop a pathbreaking &amp; cost effective mobile phone. With full integration capabilities with the hotels property management system, location based marketing, user locator and other features, this product is unique in addressing the hospitality segment.</p>
      <p>Tavelko is a telecom startup and is looking to launch its website.</p>
      <p>Tavelko specializes in providing communication solutions to the travel market. Our mission is to develop cost effective communication............</p>
    </div>
    <a class="abs read-more">
      <svg width="11" height="13" viewBox="0 0 11 13"><path d="M0 0 L11 6.5 L0 13 Z" fill="#f47f20"/></svg>
      read more
    </a>
  </main>

  <footer>
    <div class="abs footer-rule"></div>
    <span class="abs footer-nav active" style="left:417px">Home</span>
    <span class="abs footer-nav" style="left:492px">About Us</span>
    <span class="abs footer-nav" style="left:589px">Solutions</span>
    <span class="abs footer-nav" style="left:685px">Contact Us</span>
    <div class="abs panel-shadow"></div>

    <div class="abs footer-brand">
      <span class="brand-dot"></span>
      <span class="brand-name">Tavelko</span>
    </div>
    <span class="abs copyright">Copyright. All Right Reserved 2012</span>
  </footer>
</body>
</html>
```